Reputable business cards for Diplom Kauffrau, Privat und Geschäftslich

The business cards should be reputable, valuable and elegant in order to be able to use them for business. The design should also include a sophistication that is conspicuous. This could be a picture, an ornament, a sublime print or a kind of logo of the initials of my name "MD". The font should be clear and legible.
Target Market(s)
Business contacts, friends and acquaintances
Contact Information for Business Card
Diplom-Kauffrau Mirela Donat
Lindenhofweg 7 50931 Kerpen
Mobil +49 171 804 29 57
e-mail mirela.donat@postwerk.de
Colors
Designer to choose colors to be used in the design.
Requirements
Must have
- Clear and easy to read font My name in larger font than the other information Visual conspicuity / specificity
Nice to have
- Different colors
Should not have
- Ornate font, playful

```html
<!DOCTYPE html>
<html lang="de">
<head>
<meta charset="utf-8">
<title>Mirela Donat – Visitenkarte</title>
<link rel="stylesheet" href="https://fonts.googleapis.com/css2?family=Exo+2:wght@300;400;700&display=swap">
<style>
  :root {
    --backdrop: #262626;
    --card: #f3f3f1;
    --brand-blue: #0c5ea8;
    --ink-grey: #7d7d7d;
    --rule-grey: #9a9a9a;
    --white: #ffffff;
  }
  html, body {
    margin: 0;
    padding: 0;
    width: 1200px;
    height: 895px;
    overflow: hidden;
    background: var(--backdrop);
  }
  .business-card {
    position: absolute;
    left: 150px;
    top: 167px;
    width: 900px;
    height: 560px;
    background: var(--card);
    box-shadow: 0 12px 30px rgba(0,0,0,.55);
    font-family: "Exo 2", sans-serif;
    overflow: hidden;
  }
  .identity {
    position: absolute;
    top: 72px;
    left: 0;
    right: 0;
    text-align: center;
  }
  .initials-mark {
    display: inline-flex;
    align-items: center;
    gap: 14px;
    height: 90px;
  }
  .initials-square {
    width: 22px;
    height: 22px;
    background: var(--ink-grey);
  }
  .initials-text {
    font-family: "Exo 2", sans-serif;
    font-weight: 400;
    font-size: 64px;
    line-height: 1;
    color: var(--brand-blue);
  }
  .person-name {
    margin: 22px 0 0;
    font-family: "Exo 2", sans-serif;
    font-weight: 700;
    font-size: 40px;
    line-height: 1.1;
    letter-spacing: 2px;
    color: var(--brand-blue);
  }
  .job-title {
    display: flex;
    align-items: center;
    justify-content: center;
    gap: 16px;
    margin-top: 8px;
    font-weight: 400;
    font-size: 17px;
    letter-spacing: 4px;
    color: var(--ink-grey);
  }
  .job-title::before,
  .job-title::after {
    content: "";
    width: 110px;
    height: 1.5px;
    background: var(--rule-grey);
  }
  .contact-row {
    position: absolute;
    top: 345px;
    left: 0;
    right: 0;
    display: flex;
    justify-content: center;
    align-items: center;
    gap: 14px;
    font-weight: 300;
    font-size: 22px;
    color: var(--ink-grey);
  }
  .contact-icon {
    width: 30px;
    height: 30px;
  }
  .contact-divider {
    width: 1px;
    height: 44px;
    background: var(--rule-grey);
    margin: 0 6px;
  }
  .address-band {
    position: absolute;
    left: 0;
    right: 0;
    top: 430px;
    height: 50px;
    background: var(--brand-blue);
    color: var(--white);
    display: flex;
    align-items: center;
    justify-content: center;
    font-weight: 400;
    font-size: 22px;
    letter-spacing: .5px;
  }
</style>
</head>
<body>
  <main class="business-card">
    <header class="identity">
      <div class="initials-mark">
        <span class="initials-square" aria-hidden="true"></span>
        <span class="initials-text">MD</span>
      </div>
      <h1 class="person-name">MIRELA DONAT</h1>
      <div class="job-title">DIPLOM-KAUFFRAU</div>
    </header>

    <section class="contact-row">
      <span class="phone-number">+49 171 804 29 57</span>
      <svg class="contact-icon" viewBox="0 0 30 30" aria-hidden="true">
        <circle cx="15" cy="15" r="13" fill="none" stroke="var(--ink-grey)" stroke-width="1.5"/>
        <path d="M11 9 l3 0 l1 4 l-2 1.5 c1 2 2 3 4 4 l1.5 -2 l4 1 l0 3 c-7 0.5 -12 -5 -11.5 -11.5z" fill="var(--brand-blue)"/>
      </svg>
      <span class="contact-divider"></span>
      <svg class="contact-icon" viewBox="0 0 30 30" aria-hidden="true">
        <circle cx="15" cy="15" r="13" fill="none" stroke="var(--ink-grey)" stroke-width="1.5"/>
        <rect x="8" y="10" width="14" height="10" rx="1" fill="var(--brand-blue)"/>
        <path d="M8 10.5 l7 5 l7 -5" fill="none" stroke="var(--white)" stroke-width="1.3"/>
      </svg>
      <span class="email-address">mirela.donat@postwerk.de</span>
    </section>

    <footer class="address-band">Lindenhofweg 7 50931 Kerpen</footer>
  </main>
</body>
</html>
```